Trim Orchid - Weight management

Label for Weight management products.
Design: modern, clear, minimum design (less is more) – lifestyle product
Buyers: mainly female, young and middle age
I'm adding a number of blank labels for better understanding. The design should be made in a way that it looks like a product family. Because the weight management product series consist of about 10 products all together.

Target Market(s)

mainly female, young and middle age

Industry/Entity Type

Weight

Font styles to use
Sans Serif

Colors
e34297
0392cd
f37122

Requirements
Must have
• modern, clear, minimum design (less is more) – lifestyle product

```html
<!DOCTYPE html>
<html lang="de">
<head>
<meta charset="utf-8">
<title>Trim Orchid Omega 3 Label</title>
<link href="https://fonts.googleapis.com/css2?family=PT+Sans+Narrow:wght@400;700&family=Roboto+Condensed:wght@700&family=Roboto:wght@700&display=swap" rel="stylesheet">
<style>
  :root {
    --page: #ffffff;
    --label-bg: #eef5e2;
    --band-green: #b6da8c;
    --ink: #1a1a1a;
    --black: #111111;
    --tape-light: #f2d36b;
    --tape-dark: #c99a2e;
  }
  * { box-sizing: border-box; margin: 0; padding: 0; }
  html, body { width: 995px; height: 1200px; overflow: hidden; background: var(--page); }
  .canvas { position: relative; width: 995px; height: 1200px; }
  .label {
    position: absolute; left: 0; top: 410px; width: 995px; height: 380px;
    background: var(--label-bg); overflow: hidden;
    font-family: "PT Sans Narrow", sans-serif; color: var(--ink);
  }
  .label-shapes { position: absolute; inset: 0; }
  .info { position: absolute; left: 22px; top: 44px; width: 300px; }
  .info h2 { font-size: 14px; font-weight: 700; line-height: 1.2; margin-top: 3px; }
  .info p { font-size: 10.5px; line-height: 1.4; text-align: justify; }
  .info .inline { font-size: 14px; font-weight: 700; margin-top: 3px; }
  .info .inline span { font-weight: 400; font-size: 11px; }
  .contents { position: absolute; left: 22px; top: 312px; font-size: 15px; font-weight: 700; line-height: 1.3; }

  .brand-mark { position: absolute; left: 466px; top: 24px; width: 64px; height: 64px; border: 3px solid var(--ink); border-radius: 50%; }
  .brand { position: absolute; left: 324px; width: 348px; text-align: center; font-family: "Roboto", sans-serif; font-weight: 700; color: var(--ink); }
  .brand-name { top: 104px; font-size: 26px; letter-spacing: 2px; }
  .tape { position: absolute; left: 364px; top: 148px; width: 268px; height: 48px; border-radius: 4px;
    background: linear-gradient(180deg, var(--tape-light), var(--tape-dark)); }
  .product { position: absolute; left: 324px; width: 348px; text-align: center; font-family: "Roboto Condensed", sans-serif; font-weight: 700; }
  .product-name { top: 214px; font-size: 56px; line-height: 60px; color: var(--band-green); letter-spacing: 1px; }
  .product-sub { top: 292px; font-size: 32px; color: var(--ink); }
  .product-weight { top: 336px; font-size: 18px; font-family: "PT Sans Narrow", sans-serif; font-weight: 400; }

  .nutrition { position: absolute; left: 678px; top: 28px; width: 300px; }
  .nutrition h2 { font-size: 14px; font-weight: 700; line-height: 1.35; }
  .nutrition table { border-collapse: collapse; font-size: 10px; margin-top: 3px; }
  .nutrition td { padding: 0; line-height: 13.2px; vertical-align: top; }
  .nutrition td:nth-child(1) { width: 128px; }
  .nutrition td:nth-child(2) { width: 90px; }
  .notes { font-size: 10px; line-height: 1.3; margin-top: 4px; }
  .brand-small { position: absolute; left: 852px; top: 306px; width: 124px; text-align: center; font-family: "Roboto", sans-serif; font-weight: 700; font-size: 14px; line-height: 1.1; }
  .storage { position: absolute; left: 672px; top: 332px; width: 323px; height: 28px; background: var(--black); color: #fff; font-size: 9px; line-height: 1.25; text-align: center; padding: 2px 6px; }
</style>
</head>
<body>
<div class="canvas">
  <section class="label">
    <svg class="label-shapes" viewBox="0 0 995 380" width="995" height="380" aria-hidden="true">
      <defs>
        <clipPath id="hourglass">
          <path d="M324 0 L672 0 Q602 190 680 380 L316 380 Q394 190 324 0 Z"/>
        </clipPath>
      </defs>
      <path d="M324 0 L672 0 Q602 190 680 380 L316 380 Q394 190 324 0 Z" fill="var(--band-green)" stroke="var(--black)" stroke-width="1.5"/>
      <rect x="300" y="212" width="400" height="64" fill="var(--black)" clip-path="url(#hourglass)"/>
    </svg>

    <div class="info">
      <h2>Nahrungsergänzungsmittel.</h2>
      <h2>Zutaten:</h2>
      <p>Fischöl mit Omega3 Fettsäuren (18% EPA, 12% DHA); demineralisiertes Wasser, Softgel-Kapselhülle: Gelatine(Rind), Glyzerin, Vitamin E (DL-Alpha-Tocopherolacetat).</p>
      <h2>Verzehrempfehlung:</h2>
      <p>1x zwei Kapseln pro Tag</p>
      <div class="inline">Gesamtgewicht Kapsel: <span>1450 mg</span></div>
      <h2>Hinweise:</h2>
      <p>Empfohlene tägliche Verzehrmenge nicht überschreiten. Nicht als Ersatz für eine ausgewogene und abwechslungsreiche Ernährung verwenden. Außerhalb der Reichweite von kleinen Kindern lagern.</p>
      <h2>Allergen-Kennzeichnung:</h2>
      <p>enthält Zutaten aus Fisch: Sardine, Makrele und Sardelle</p>
    </div>
    <div class="contents">INHALT: 200 STÜCK (À 1,450G)<br>NETTOGEWICHT PRO DOSE: ℮ 290G</div>

    <div class="brand-mark"></div>
    <div class="brand brand-name">TRIM ORCHID</div>
    <div class="tape" role="img" aria-label="Gold measuring tape wrapped around the waist of the label"></div>
    <div class="product product-name">OMEGA 3</div>
    <div class="product product-sub">18 DHA &amp; 12 EPA</div>
    <div class="product product-weight">290g</div>

    <div class="nutrition">
      <h2>Nährwerte pro 100gpro Kapsel<br>(1450 mg)</h2>
      <table>
        <tr><td>Energie</td><td>799 kJ (191,2 kcal)</td><td>11,6 kJ (2,8 kcal)</td></tr>
        <tr><td>Fett</td><td>6,7g</td><td>97mg</td></tr>
        <tr><td>- davon gesättigte</td><td></td><td></td></tr>
        <tr><td>Fettsäuren</td><td>5,3g</td><td>77mg</td></tr>
        <tr><td>Kohlenhydrate</td><td>26,5g</td><td>384mg</td></tr>
        <tr><td>- davon Zucker</td><td>&lt; 0,1g</td><td>&lt; 0,1mg</td></tr>
        <tr><td>Eiweiß</td><td>16,9g</td><td>245mg</td></tr>
        <tr><td>Salz</td><td>&lt; 0,1g</td><td>&lt; 0,1mg</td></tr>
        <tr><td>Fischöl</td><td>69,0g</td><td>1000mg</td></tr>
        <tr><td>- davon Omega 3</td><td>20,7g</td><td>300mg</td></tr>
        <tr><td>- davon EPA*</td><td>12,4g</td><td>180mg</td></tr>
        <tr><td>- davon DHA**</td><td>8,3g</td><td>120mg</td></tr>
        <tr><td>Vitamin E</td><td>827,6mg</td><td>12mg</td></tr>
        <tr><td>- davon NRV***</td><td>5172 %</td><td>75 %</td></tr>
      </table>
      <p class="notes">* EPA = Eicosapentaensäure<br>** DHA = Docosahexaensäure<br>*** NRV = % der Nährstoffbezugswerte<br>(nach VO (EG) Nr. 1169/2011)</p>
    </div>
    <div class="brand-small">TRIM ORCHID</div>
    <div class="storage">Bei Raumtemperatur (bis 21°C), trocken und vor Sonneneinstrahlung geschützt lagern. LOT-Nr. / Mindestens haltbar bis Ende: Siehe Dosenboden.</div>
  </section>
</div>
</body>
</html>
```